Business cards and letterhead
UK size business cards/letterhead
Project: Business cards and letterhead
Business cards and letterhead - Information Technology
Creative Brief
Professional
Gareth Pellow
Director
148 Ashcombe Lane Twickenham Middlesex TW4 3QR
gareth.pellow@corvalisen.com
www.corvalisen.com
Note business card needs to be UK-sized (i.e. 85 x 55)/double sided, and the letterhead suitable for A4 paper Back of card can contain some/all of suggested text, depending upon how well it fits
ECM Consultancy Services - Project Management and Delivery - Implementation Planning - Data Conversion Management - Existing System Reviews - Software Design and Development - Test Strategy Definition and Execution

```html
<!DOCTYPE html>
<html lang="en">
<head>
<meta charset="utf-8">
<title>Corvalisen Stationery</title>
<link href="https://fonts.googleapis.com/css2?family=Montserrat:wght@400;600;700&family=Open+Sans:wght@400;600&display=swap" rel="stylesheet">
<style>
:root{
  --blue:#1a8fc4;
  --blue-dark:#0e5f8a;
  --navy:#1d3550;
  --ink:#2a2f36;
  --grey:#8c949c;
  --grey-dark:#5a6068;
  --paper:#ffffff;
  --bg:#ffffff;
  --faint:#eef1f4;
}
*{margin:0;padding:0;box-sizing:border-box}
html,body{width:1200px;height:437px;overflow:hidden;background:var(--bg)}
body{position:relative;font-family:"Open Sans",sans-serif;color:var(--ink)}
.piece{position:absolute;background:var(--paper);box-shadow:0 1px 4px rgba(0,0,0,.25);overflow:hidden}
.piece svg.shape{position:absolute;inset:0;width:100%;height:100%}
.caption{position:absolute;font-size:5px;color:var(--grey);text-align:center;width:120px}
.brand{position:absolute;display:flex;align-items:center;gap:3px;font-family:"Montserrat",sans-serif;font-weight:700;color:var(--navy);letter-spacing:.5px}
.brand .dot{border-radius:50%;background:var(--blue)}
.faint-circle{position:absolute;border-radius:50%;border:10px solid var(--faint)}
.tiny{font-size:3.6px;line-height:1.5;color:var(--grey-dark)}
.card-name{font-family:"Montserrat",sans-serif;font-weight:600;font-size:5px;color:var(--navy)}
.card-role{font-size:3.6px;color:var(--grey)}
.services-title{font-family:"Montserrat",sans-serif;font-weight:600;font-size:4.6px;color:var(--blue)}
.services li{list-style:none;font-size:3.4px;line-height:1.6}
.card-back-blue{background:var(--blue)}
.card-back-blue .services-title,.card-back-blue .services li{color:#fff}
</style>
</head>
<body>

<!-- Business card front -->
<div class="piece card-front" style="left:29px;top:139px;width:91px;height:58px">
  <svg class="shape" viewBox="0 0 91 58" preserveAspectRatio="none">
    <path d="M0 0 H14 Q6 29 14 58 H0Z" fill="var(--blue-dark)"/>
    <path d="M0 0 H10 Q3 29 10 58 H0Z" fill="var(--blue)"/>
  </svg>
  <div class="brand" style="left:20px;top:26px;font-size:7px"><span class="dot" style="width:6px;height:6px"></span>CORVALISEN</div>
  <div style="position:absolute;left:52px;top:6px">
    <div class="card-name">Gareth Pellow</div>
    <div class="card-role">Director</div>
  </div>
  <div class="tiny" style="position:absolute;left:56px;top:36px;width:33px">148 Ashcombe Lane<br>Twickenham TW4 3QR<br>gareth.pellow@corvalisen.com<br>www.corvalisen.com</div>
</div>
<div class="caption" style="left:15px;top:200px">Business Card Front</div>

<!-- Business card back, white -->
<div class="piece card-back" style="left:29px;top:216px;width:91px;height:58px">
  <svg class="shape" viewBox="0 0 91 58" preserveAspectRatio="none">
    <path d="M0 0 H8 Q2 29 8 58 H0Z" fill="var(--blue)"/>
  </svg>
  <div style="position:absolute;left:14px;top:7px">
    <div class="services-title">ECM Consultancy Services</div>
    <ul class="services" style="margin-top:2px">
      <li>- Project Management and Delivery</li>
      <li>- Implementation Planning</li>
      <li>- Data Conversion Management</li>
      <li>- Existing System Reviews</li>
      <li>- Software Design and Development</li>
      <li>- Test Strategy Definition and Execution</li>
    </ul>
  </div>
</div>
<div class="caption" style="left:15px;top:277px">Back Card Design One</div>

<!-- Business card back, blue -->
<div class="piece card-back card-back-blue" style="left:29px;top:298px;width:91px;height:58px">
  <div style="position:absolute;left:8px;top:7px">
    <div class="services-title">ECM Consultancy Services</div>
    <ul class="services" style="margin-top:2px">
      <li>- Project Management and Delivery</li>
      <li>- Implementation Planning</li>
      <li>- Data Conversion Management</li>
      <li>- Existing System Reviews</li>
      <li>- Software Design and Development</li>
      <li>- Test Strategy Definition and Execution</li>
    </ul>
  </div>
</div>
<div class="caption" style="left:15px;top:359px">Back Card Design Two</div>

<!-- Letterhead one -->
<div class="piece letterhead" style="left:163px;top:34px;width:173px;height:362px">
  <svg class="shape" viewBox="0 0 173 362" preserveAspectRatio="none">
    <path d="M0 0 H60 Q20 8 10 60 L0 80Z" fill="var(--blue-dark)"/>
    <path d="M0 0 H50 Q14 10 6 58 L0 70Z" fill="var(--blue)"/>
    <path d="M173 362 H120 Q160 352 167 310 L173 300Z" fill="var(--blue)"/>
  </svg>
  <div class="brand" style="left:26px;top:18px;font-size:10px"><span class="dot" style="width:8px;height:8px"></span>CORVALISEN</div>
  <div class="tiny" style="position:absolute;left:112px;top:14px;width:58px">148 Ashcombe Lane<br>Twickenham<br>Middlesex TW4 3QR<br>gareth.pellow@corvalisen.com<br>www.corvalisen.com</div>
  <div class="faint-circle" style="left:36px;top:110px;width:100px;height:100px"></div>
  <div class="tiny" style="position:absolute;left:10px;top:344px;width:110px;text-align:center">Registered in England · Company No. 0000000</div>
</div>
<div class="caption" style="left:190px;top:400px">Letterhead Option One</div>

<!-- Letterhead two -->
<div class="piece letterhead" style="left:497px;top:34px;width:173px;height:362px">
  <svg class="shape" viewBox="0 0 173 362" preserveAspectRatio="none">
    <path d="M0 0 H40 Q10 20 0 90Z" fill="var(--blue)"/>
    <path d="M0 362 H70 Q20 350 0 300Z" fill="var(--blue-dark)"/>
  </svg>
  <div class="brand" style="left:48px;top:26px;font-size:11px"><span class="dot" style="width:8px;height:8px"></span>CORVALISEN</div>
  <div class="faint-circle" style="left:36px;top:110px;width:100px;height:100px"></div>
  <div class="tiny" style="position:absolute;left:40px;top:340px;width:125px;text-align:center">148 Ashcombe Lane Twickenham Middlesex TW4 3QR<br>gareth.pellow@corvalisen.com · www.corvalisen.com</div>
</div>
<div class="caption" style="left:524px;top:400px">Letterhead Option Two</div>

<!-- Envelopes -->
<div class="piece envelope" style="left:720px;top:34px;width:276px;height:72px;background:#e9ebed">
  <svg class="shape" viewBox="0 0 276 72" preserveAspectRatio="none">
    <defs><linearGradient id="flapGrey" x1="0" y1="0" x2="0" y2="1"><stop offset="0" stop-color="#3d4248"/><stop offset="1" stop-color="#7a8088"/></linearGradient></defs>
    <path d="M0 0 H276 L150 46 Q138 50 126 46Z" fill="url(#flapGrey)"/>
  </svg>
</div>
<div class="piece envelope" style="left:720px;top:120px;width:276px;height:72px;background:#f2f4f6">
  <svg class="shape" viewBox="0 0 276 72" preserveAspectRatio="none">
    <defs><linearGradient id="flapBlue" x1="0" y1="0" x2="0" y2="1"><stop offset="0" stop-color="var(--blue-dark)"/><stop offset="1" stop-color="var(--blue)"/></linearGradient></defs>
    <path d="M0 0 H276 L150 46 Q138 50 126 46Z" fill="url(#flapBlue)"/>
  </svg>
</div>
<div class="piece envelope" style="left:720px;top:211px;width:276px;height:76px;background:#fafafa">
  <svg class="shape" viewBox="0 0 276 76" preserveAspectRatio="none">
    <path d="M0 0 H276 L150 48 Q138 52 126 48Z" fill="#e4e7ea"/>
  </svg>
</div>
<div class="piece envelope-card" style="left:720px;top:259px;width:216px;height:125px">
  <svg class="shape" viewBox="0 0 216 125" preserveAspectRatio="none">
    <path d="M0 125 V80 Q40 110 216 112 V125Z" fill="var(--blue-dark)"/>
    <path d="M0 80 Q10 100 40 108 Q10 110 0 125Z" fill="var(--blue)"/>
  </svg>
  <div class="brand" style="left:24px;top:64px;font-size:10px"><span class="dot" style="width:8px;height:8px"></span>CORVALISEN</div>
  <div class="tiny" style="position:absolute;left:24px;top:80px;width:120px">148 Ashcombe Lane Twickenham Middlesex TW4 3QR</div>
</div>
<div class="caption" style="left:800px;top:392px">Envelope Design</div>

</body>
</html>
```